Business card design for strategy and management consulting company. Would like to have a clean and professional business card, based on the attached logo. The company is a strategy and management consulting company focusing on sustainable business modlels based on economic, social and environmental market opportunities. Preferably the logo should be included on both sides of the design.

Industry/Entity Type

Business

Contact Information for Business Card

Håvard Lilleby, CEO/Management consultant
havard.lilleby@quarvenpartners.example
Mob: +47 948 26 317
Office: Vikfjell gate 14, pb 312 sentrum, N-0172 Oslo Norway

Requirements
Must have
• Include attached logo
Nice to have
• Would like to have the logo on both sides
Should not have
• Many colours.

```html
<!DOCTYPE html>
<html lang="en">
<head>
<meta charset="utf-8">
<title>Quarven business card</title>
<link rel="stylesheet" href="https://fonts.googleapis.com/css2?family=Roboto:wght@400;500;700&family=Roboto+Condensed:wght@400;700&display=swap">
<style>
  :root {
    --backdrop: #e4e2de;
    --card-dark: #1f2022;
    --card-dark-deep: #18191b;
    --accent-yellow: #ffdb1f;
    --text-light: #ffffff;
    --text-dim: #c9c9c9;
    --text-dark: #1d1d1d;
  }
  * { margin: 0; padding: 0; box-sizing: border-box; }
  html, body {
    width: 1200px; height: 911px; overflow: hidden;
    background: var(--backdrop);
  }
  .sheet {
    width: 1200px; height: 911px;
    display: flex; flex-direction: column;
    align-items: center; justify-content: center; gap: 40px;
  }
  .card {
    position: relative;
    width: 700px; height: 400px;
    background: var(--card-dark);
    overflow: hidden;
    box-shadow: 0 6px 18px rgba(0,0,0,0.18);
    font-family: "Roboto", sans-serif;
    color: var(--text-light);
  }
  .card--back { background: var(--card-dark-deep); }

  .wordmark {
    position: absolute;
    display: flex; align-items: center; gap: 10px;
    font-family: "Roboto", sans-serif;
    font-weight: 700;
    color: var(--text-light);
    letter-spacing: -1px;
    line-height: 1;
  }
  .wordmark__dot {
    width: 14px; height: 14px; border-radius: 50%;
    background: var(--accent-yellow);
    flex: none;
  }
  .card--front .wordmark { left: 58px; top: 62px; font-size: 94px; }

  .identity { position: absolute; left: 62px; top: 190px; }
  .identity__name {
    font-family: "Roboto Condensed", sans-serif;
    font-weight: 700; font-size: 24px;
    color: var(--accent-yellow);
  }
  .identity__role {
    margin-top: 4px;
    font-family: "Roboto Condensed", sans-serif;
    font-size: 18px; color: var(--text-light);
  }

  .accent-band { position: absolute; inset: 0; }

  .contact {
    position: absolute; left: 40px; bottom: 22px;
    font-family: "Roboto Condensed", sans-serif;
    font-size: 14px; color: var(--text-dark);
    line-height: 1.55;
  }
  .contact__row { display: flex; align-items: center; gap: 5px; white-space: nowrap; }
  .contact__row svg { flex: none; }
  .contact__gap { width: 8px; }

  .card--back .wordmark {
    left: 50%; top: 50%;
    transform: translate(-50%, -42%);
    font-size: 110px;
  }
  .site-line {
    position: absolute; left: 50px; top: 46px;
    font-size: 14px; letter-spacing: 6px;
    color: var(--text-dim);
  }
</style>
</head>
<body>
<main class="sheet">

  <section class="card card--front">
    <svg class="accent-band" width="700" height="400" viewBox="0 0 700 400" aria-hidden="true">
      <path d="M0 318 Q 400 320 700 120 L700 400 L0 400 Z" fill="var(--accent-yellow)"/>
    </svg>

    <div class="wordmark">Quarven<span class="wordmark__dot"></span></div>

    <div class="identity">
      <p class="identity__name">Håvard Lilleby</p>
      <p class="identity__role">CEO/Management consultant</p>
    </div>

    <div class="contact">
      <p class="contact__row">Vikfjell gate 14, pb 312 sentrum, N-0172 Oslo Norway</p>
      <p class="contact__row">
        <svg width="10" height="14" viewBox="0 0 10 14" aria-hidden="true"><rect x="1" y="0.8" width="8" height="12.4" rx="1.5" fill="none" stroke="currentColor" stroke-width="1.4"/><circle cx="5" cy="11" r="0.9" fill="currentColor"/></svg>
        +47 948 26 317
        <span class="contact__gap"></span>
        <svg width="14" height="10" viewBox="0 0 14 10" aria-hidden="true"><rect x="0" y="0" width="14" height="10" rx="1" fill="currentColor"/><path d="M1 1 L7 6 L13 1" fill="none" stroke="var(--accent-yellow)" stroke-width="1.2"/></svg>
        havard.lilleby@quarvenpartners.example
        <span class="contact__gap"></span>
        <svg width="12" height="12" viewBox="0 0 12 12" aria-hidden="true"><circle cx="6" cy="6" r="5.3" fill="none" stroke="currentColor" stroke-width="1.2"/><ellipse cx="6" cy="6" rx="2.3" ry="5.3" fill="none" stroke="currentColor" stroke-width="1"/><path d="M0.7 6 H11.3" stroke="currentColor" stroke-width="1"/></svg>
        www.quarvenpartners.example
      </p>
    </div>
  </section>

  <section class="card card--back">
    <p class="site-line">www.quarvenpartners.example</p>
    <div class="wordmark">Quarven<span class="wordmark__dot"></span></div>
  </section>

</main>
</body>
</html>
```